Bref créative
Tri-Valley Marketing Materials
Business Card, Letterhead, Envelope, PPT template
Simple
Marguerite Olson Trevane, M.S. CCC-SLP
President, Owner and SLP Certified Bilingual Speech Language Pathologist
48770 Hollin Avenue, Suite #300 Cedar Hollow, Oregon 97412
trivalleyslp@mailbox-example.net
www.trivalleyslp-example.net
Please include the following phrase on business card and letterhead:
Progressive clinical treatment for speech and language deficiencies, feeding aversions, swallowing problems, sensory issues, fine motor difficulties, visual processing impairments, tortocolis and developmental delays
I am uploading 2 AI files for your use in the design of Tri-Valley Marketing Materials.
I think the blue background logo might be more appealing for the letterhead, business card, and PPT template designs...

```html
<!DOCTYPE html>
<html lang="en">
<head>
<meta charset="utf-8">
<title>Tri-Valley Business Card</title>
<link href="https://fonts.googleapis.com/css2?family=Crimson+Text:wght@400;600;700&display=swap" rel="stylesheet">
<style>
  :root{
    --page:#ececec;
    --card-white:#ffffff;
    --brand-blue:#22399a;
    --brand-blue-deep:#16267a;
    --brand-blue-light:#3b55c4;
    --text-grey:#7a7a7a;
    --accent-orange:#e39a2d;
    --accent-sun:#f2b233;
  }
  *{box-sizing:border-box;margin:0;padding:0}
  html,body{width:1200px;height:1030px;overflow:hidden}
  body{background:var(--page);font-family:"Crimson Text",serif;position:relative}

  .card{position:absolute;left:220px;width:760px;height:434px;border-radius:22px;overflow:hidden;
        box-shadow:0 6px 18px rgba(0,0,0,.18)}
  .card--front{top:60px;background:var(--card-white)}
  .card--back{top:540px;background:radial-gradient(ellipse at 50% 40%,var(--brand-blue-light) 0%,var(--brand-blue) 45%,var(--brand-blue-deep) 100%)}

  .front__edge{position:absolute;left:0;top:250px;width:12px;height:110px;background:var(--brand-blue)}

  .brand{position:absolute;left:44px;top:70px;width:260px}
  .brand__dot{width:64px;height:64px;border-radius:50%;background:var(--accent-sun);margin:0 0 14px 40px}
  .brand__name{font-weight:700;color:var(--brand-blue);font-size:25px;line-height:1.05}

  .contact{position:absolute;left:44px;top:278px;font-size:14.5px;line-height:1.35;color:var(--text-grey)}
  .contact__row{display:flex;align-items:center;gap:6px}
  .contact__row svg{width:12px;height:12px;flex:none}
  .contact__web{color:var(--accent-orange)}

  .person{position:absolute;left:360px;top:58px;width:360px;text-align:center}
  .person__name{font-weight:700;color:var(--brand-blue);font-size:24px;line-height:1.15}
  .person__title{color:var(--text-grey);font-size:15px;line-height:1.3;margin-top:8px}
  .person__services{color:var(--text-grey);font-size:14.5px;line-height:1.35;margin-top:46px}

  .back__mark{position:absolute;left:50%;top:50%;transform:translate(-50%,-50%);text-align:center}
  .back__circle{width:110px;height:110px;border-radius:50%;border:6px solid #fff;margin:0 auto 14px}
  .back__name{color:#fff;font-weight:700;font-size:30px}
</style>
</head>
<body>

<section class="card card--front">
  <div class="front__edge"></div>

  <div class="brand">
    <div class="brand__dot"></div>
    <div class="brand__name">Tri-Valley Speech Occupational &amp; Physical Therapy</div>
  </div>

  <div class="contact">
    <div>48770 Hollin Avenue, Suite #300</div>
    <div>Cedar Hollow, Oregon 97412</div>
    <div class="contact__row">
      <svg viewBox="0 0 12 12" aria-hidden="true"><path d="M3 1l2 2-1 1.5c.8 1.6 1.9 2.7 3.5 3.5L9 7l2 2-1.5 2C5 10.5 1.5 7 1 2.5z" fill="#7a7a7a"/></svg>
      <span>954-555-0148 &nbsp;|&nbsp; F 954-555-0172</span>
    </div>
    <div class="contact__row">
      <svg viewBox="0 0 12 12" aria-hidden="true"><rect x="1" y="2.5" width="10" height="7" fill="none" stroke="#7a7a7a"/><path d="M1 2.5l5 4 5-4" fill="none" stroke="#7a7a7a"/></svg>
      <span>trivalleyslp@mailbox-example.net</span>
    </div>
    <div class="contact__web">www.trivalleyslp-example.net</div>
  </div>

  <div class="person">
    <div class="person__name">Marguerite Olson Trevane,<br>M.S. CCC-SLP</div>
    <div class="person__title">President, Owner and SLP Certified<br>Bilingual Speech Language Pathologist</div>
    <p class="person__services">Progressive clinical treatment for speech and language deficiencies, feeding aversions, swallowing problems, sensory issues, fine motor difficulties, visual processing impairments, tortocolis and developmental delays</p>
  </div>
</section>

<section class="card card--back">
  <div class="back__mark">
    <div class="back__circle"></div>
    <div class="back__name">Tri-Valley</div>
  </div>
</section>

</body>
</html>
```